my personal cards just intrducing my self

Massage Therapy to get my name out their

Target Market(s)

40 year olds who enjoy massage

Industry/Entity Type

Massage

Contact Information for Business Card

Leonard T Vasquelle
LMT-Licensed Massage Therapist
*Swedish *Deep Tissue *Prenatal
*Reflexology *Chair and more

(602)-347-2916
leonardvasquelle@mailorbit.net

Font styles to use
Serif

Colors
0456a4
6b449b

```html
<!DOCTYPE html>
<html lang="en">
<head>
<meta charset="utf-8">
<title>Leonard T Vasquelle LMT – Business Card</title>
<link href="https://fonts.googleapis.com/css2?family=Marcellus&family=Poiret+One&display=swap" rel="stylesheet">
<style>
  :root {
    --backdrop-top: #aeeef9;
    --backdrop-bottom: #d3f5fb;
    --card-light: #eceef0;
    --card-mid: #d9dcdf;
    --card-dark: #c9cdd1;
    --accent-blue: #3aa9e0;
    --ink: #1b1b1b;
    --ink-soft: #3a3a3a;
  }
  * { margin: 0; padding: 0; box-sizing: border-box; }
  html, body { width: 1200px; height: 960px; overflow: hidden; }
  body {
    position: relative;
    background: linear-gradient(160deg, var(--backdrop-top), var(--backdrop-bottom));
  }
  .card {
    position: absolute;
    top: 290px;
    width: 460px;
    height: 280px;
    background:
      repeating-linear-gradient(0deg, rgba(255,255,255,0.18) 0 1px, rgba(0,0,0,0.02) 1px 3px),
      linear-gradient(100deg, var(--card-mid), var(--card-light) 35%, var(--card-dark) 60%, var(--card-light) 85%, var(--card-mid));
    text-align: center;
  }
  .card--back { left: 110px; }
  .card--front { left: 630px; }
  .services {
    margin-top: 28px;
    font-family: "Poiret One", sans-serif;
    font-size: 21px;
    line-height: 24px;
    color: var(--accent-blue);
    list-style: none;
  }
  .contact {
    margin-top: 46px;
    font-family: "Marcellus", serif;
    font-size: 16px;
    line-height: 28px;
    color: var(--accent-blue);
  }
  .emblem {
    display: block;
    margin: 22px auto 0;
  }
  .holder-name {
    margin-top: 8px;
    font-family: "Marcellus", serif;
    font-size: 17px;
    color: var(--ink);
  }
  .holder-title {
    font-family: "Poiret One", sans-serif;
    font-size: 17px;
    color: var(--ink-soft);
  }
</style>
</head>
<body>
  <section class="card card--back">
    <ul class="services">
      <li>*Swedish</li>
      <li>*Deep Tissue</li>
      <li>*Prenatal Reflexology</li>
      <li>*Sports*</li>
      <li>and more...</li>
    </ul>
    <div class="contact">
      <p class="contact-phone">(602)-347-2916</p>
      <p class="contact-email">leonardvasquelle@mailorbit.net</p>
    </div>
  </section>

  <section class="card card--front">
    <svg class="emblem" width="210" height="190" viewBox="0 0 210 190" role="img" aria-label="Line illustration of a therapist massaging a client lying on a table, inside a circle">
      <defs>
        <radialGradient id="emblemFill" cx="50%" cy="45%" r="55%">
          <stop offset="0%" stop-color="#cfe9f6"/>
          <stop offset="100%" stop-color="#b9def2"/>
        </radialGradient>
      </defs>
      <circle cx="105" cy="95" r="92" fill="url(#emblemFill)"/>
    </svg>
    <p class="holder-name">Leonard T Vasquelle LMT</p>
    <p class="holder-title">Licensed Massage Therapist</p>
  </section>
</body>
</html>
```